truck and trailer business Wrap Design

needing a redisgn of our truck and trailer wraps, i have attached the current trailer wrap design and pictures of the new trailer needing a wrap design. trailer is 26ft v nose. 8.5 wide and 7.5ft tall need the trucks that pull the trailers to match. 2018 q-380 long bed. i have attached pictures of the truck. 2009 ZEMO 26 FT BOX

Industry/Entity Type

Insulation

Colors

Designer to choose colors to be used in the design.

Requirements
Must have
• wrap needs to be unique and stand out like our current wrap

```html
<!DOCTYPE html>
<html lang="en">
<head>
<meta charset="utf-8">
<title>Momentum Spray Foam – Fleet Wrap Set</title>
<link rel="stylesheet" href="https://fonts.googleapis.com/css2?family=Exo+2:ital,wght@0,800;1,700;1,800&display=swap">
<style>
:root{
  --ink:#0b0c0f;
  --panel:#121317;
  --blue:#1f4fb8;
  --blue-deep:#143a94;
  --blue-bright:#2f6fe0;
  --white:#ffffff;
  --silver:#d9dde3;
  --page:#eef0f3;
  --photo-a:#4a5566;
  --photo-b:#1b2130;
}
*{margin:0;padding:0;box-sizing:border-box}
html,body{width:1200px;height:1200px;overflow:hidden;background:var(--page)}
body{font-family:"Exo 2",sans-serif;color:var(--white);position:relative}
.panel{position:absolute;background:var(--panel);overflow:hidden;border:3px solid var(--silver)}
.tagline{font-style:italic;font-weight:700;letter-spacing:.04em;text-transform:uppercase}
.brand{font-weight:800;text-transform:uppercase;line-height:.95;color:var(--blue-bright);letter-spacing:.06em}
.brand-sub{font-weight:800;text-transform:uppercase;color:var(--white);letter-spacing:.06em}
.phone{font-style:italic;font-weight:800;letter-spacing:.02em}
.web{font-style:italic;font-weight:700;color:var(--blue-bright);text-transform:uppercase}
.strap{background:var(--blue);font-style:italic;font-weight:800;text-transform:uppercase;text-align:center}
.social{display:flex;align-items:center;justify-content:center;gap:6px;font-style:italic;font-weight:700;color:var(--blue-bright);text-transform:uppercase}
.social .sq{width:9px;height:9px;background:var(--blue)}
.photo{position:absolute;background:linear-gradient(135deg,var(--photo-a),var(--photo-b))}

.side-header{position:absolute;top:0;left:0;right:0;height:26px;background:var(--blue-deep);text-align:right;padding:5px 18px 0 0;font-size:13px}
.side-copy{position:absolute;text-align:center}
.side-copy .rule{height:2px;background:var(--white);margin:3px auto}

.rear-head{position:absolute;top:0;left:0;right:0;height:78px}
.rear-head svg{position:absolute;inset:0}
.rear-head p{position:relative;text-align:center;font-size:17px;line-height:1.2;padding-top:12px}
.rear-body{position:absolute;left:0;right:0;text-align:center}

.pickup-wrap{position:absolute;left:20px;top:640px;width:1160px;height:520px;border:3px solid var(--silver);overflow:hidden;background:var(--white)}
.pickup-wrap svg{display:block}
</style>
</head>
<body>

<section class="panel box-side" style="left:20px;top:20px;width:620px;height:220px">
  <div class="photo" role="img" aria-label="Photo of an installer in protective suit spraying foam insulation" style="left:0;top:0;width:170px;height:220px"></div>
  <svg width="620" height="220" style="position:absolute;left:0;top:0">
    <polygon points="0,0 230,0 110,110 0,110" fill="var(--blue)" opacity=".85"/>
    <polygon points="170,0 240,0 60,220 0,220" fill="var(--panel)"/>
    <line x1="120" y1="220" x2="250" y2="90" stroke="var(--white)" stroke-width="2"/>
  </svg>
  <div class="side-header tagline">Spray Foam - Fiberglass - Insulation - Roofing</div>
  <div class="side-copy" style="left:230px;top:44px;width:370px">
    <div class="brand" style="font-size:30px">Momentum</div>
    <div class="brand-sub" style="font-size:24px">Spray Foam</div>
    <div class="rule" style="width:260px"></div>
    <div class="phone" style="font-size:32px;margin-top:6px">555-014-7720</div>
    <div class="web" style="font-size:12px;margin-top:6px">momentumsprayfoam.net</div>
    <div class="strap" style="font-size:8px;padding:3px;margin:6px 0 0 190px;width:170px">DFW Premier Insulation Company</div>
  </div>
</section>

<section class="panel trailer-side" style="left:660px;top:20px;width:520px;height:220px">
  <div class="photo" role="img" aria-label="Photo of an installer spraying foam insulation" style="left:0;top:0;width:130px;height:220px"></div>
  <div class="photo" role="img" aria-label="Faded photo of insulation crew at work" style="left:360px;top:26px;width:160px;height:194px;opacity:.55"></div>
  <svg width="520" height="220" style="position:absolute;left:0;top:0">
    <polygon points="0,0 180,0 90,90 0,90" fill="var(--blue)" opacity=".85"/>
    <polygon points="130,0 190,0 40,220 0,220" fill="var(--panel)"/>
    <rect x="0" y="168" width="520" height="6" fill="var(--blue)"/>
    <rect x="380" y="40" width="90" height="160" fill="none" stroke="var(--silver)" stroke-width="3"/>
  </svg>
  <div class="side-header tagline" style="font-size:12px">Spray Foam - Fiberglass - Insulation - Roofing</div>
  <div class="side-copy" style="left:150px;top:44px;width:240px">
    <div class="brand" style="font-size:24px">Momentum</div>
    <div class="brand-sub" style="font-size:19px">Spray Foam</div>
    <div class="rule" style="width:200px"></div>
    <div class="phone" style="font-size:27px;margin-top:6px">555-014-7720</div>
    <div class="web" style="font-size:10px;margin-top:4px">momentumsprayfoam.net</div>
    <div class="tagline" style="font-size:8px;margin-top:4px">DFW Premier Insulation Company</div>
  </div>
</section>

<section class="panel box-front" style="left:20px;top:260px;width:280px;height:80px">
  <div class="strap" style="font-size:10px;padding:4px">momentumsprayfoam.net</div>
  <div style="text-align:center;margin-top:8px">
    <div class="brand" style="font-size:16px">Momentum</div>
    <div class="brand-sub" style="font-size:13px">Spray Foam</div>
  </div>
</section>

<section class="panel trailer-nose" style="left:20px;top:360px;width:280px;height:240px">
  <div class="strap" style="font-size:10px;padding:4px">momentumsprayfoam.net</div>
  <div class="photo" role="img" aria-label="Faded photo of insulation crew at work" style="left:0;top:24px;width:280px;height:216px;opacity:.35"></div>
  <div style="position:absolute;left:0;right:0;top:150px;text-align:center">
    <div class="brand" style="font-size:16px">Momentum</div>
    <div class="brand-sub" style="font-size:13px">Spray Foam</div>
  </div>
</section>

<section class="panel box-rear" style="left:320px;top:260px;width:420px;height:340px">
  <div class="rear-head">
    <svg width="414" height="78"><polygon points="0,0 414,0 414,58 230,58 207,74 184,58 0,58" fill="var(--blue-deep)"/></svg>
    <p class="tagline">Spray Foam - Fiberglass<br>Insulation - Roofing</p>
  </div>
  <div class="rear-body" style="top:100px">
    <div class="brand" style="font-size:34px">Momentum</div>
    <div class="brand-sub" style="font-size:26px">Spray Foam</div>
    <div style="height:2px;width:300px;background:var(--white);margin:4px auto"></div>
    <div class="phone" style="font-size:38px;margin-top:10px">555-014-7720</div>
    <div class="strap" style="font-size:11px;padding:5px;margin-top:16px">DFW Premier Insulation Company</div>
    <div class="social" style="font-size:12px;margin-top:10px"><span class="sq"></span>momentumsprayfoam</div>
  </div>
</section>

<section class="panel trailer-rear" style="left:760px;top:260px;width:420px;height:340px">
  <div class="rear-head">
    <svg width="414" height="78"><polygon points="0,0 414,0 414,58 230,58 207,74 184,58 0,58" fill="var(--blue-deep)"/></svg>
    <p class="tagline">Spray Foam - Fiberglass<br>Insulation - Roofing</p>
  </div>
  <div class="rear-body" style="top:100px">
    <div class="brand" style="font-size:34px">Momentum</div>
    <div class="brand-sub" style="font-size:26px">Spray Foam</div>
    <div style="height:2px;width:300px;background:var(--white);margin:4px auto"></div>
    <div class="phone" style="font-size:38px;margin-top:10px">555-014-7720</div>
    <div class="strap" style="font-size:11px;padding:5px;margin-top:16px">DFW Premier Insulation Company</div>
    <div class="social" style="font-size:12px;margin-top:10px"><span class="sq"></span>momentumsprayfoam</div>
  </div>
  <div style="position:absolute;left:0;right:0;bottom:0;height:8px;background:repeating-linear-gradient(90deg,#d22 0 20px,var(--white) 20px 40px)"></div>
</section>

<section class="pickup-wrap">
  <svg width="1154" height="514" viewBox="0 0 1160 520" preserveAspectRatio="none">
    <rect width="1160" height="520" fill="var(--white)"/>
    <polygon points="0,0 1160,0 1160,110 0,330" fill="var(--blue)"/>
    <polygon points="0,330 1160,110 1160,122 0,342" fill="var(--ink)"/>
    <polygon points="480,520 1160,250 1160,520" fill="var(--ink)"/>
    <polygon points="440,520 1160,236 1160,250 480,520" fill="var(--blue)"/>
    <g transform="rotate(-10.7 500 235)" font-family="'Exo 2',sans-serif">
      <text x="240" y="222" font-size="17" font-style="italic" font-weight="700" fill="var(--white)">DFW PREMIER INSULATION COMPANY</text>
      <text x="220" y="305" font-size="66" font-weight="800" fill="var(--blue-bright)" letter-spacing="4">MOMENTUM</text>
      <text x="280" y="362" font-size="48" font-weight="800" fill="var(--ink)" letter-spacing="3">SPRAY FOAM</text>
      <text x="450" y="400" font-size="18" font-style="italic" font-weight="700" fill="var(--ink)">MOMENTUMSPRAYFOAM.NET</text>
    </g>
    <text x="780" y="270" transform="rotate(-10.7 780 270)" font-family="'Exo 2',sans-serif" font-size="50" font-style="italic" font-weight="800" fill="var(--blue)">555-014-7720</text>
    <rect x="945" y="390" width="22" height="22" fill="var(--blue)"/>
    <g font-family="'Exo 2',sans-serif" font-size="15" font-style="italic" font-weight="800" fill="var(--white)">
      <text x="1000" y="380">SPRAY FOAM</text>
      <text x="1000" y="402">FIBERGLASS</text>
      <text x="1000" y="424">INSULATION</text>
      <text x="1000" y="446">ROOFING</text>
    </g>
  </svg>
</section>

</body>
</html>
```